Mailer Postcard for Potential Bankruptcy Clients

The postcard will be printed at 8.5"x6" to abide by the specification at the following link: https://www.mailtrelbo.com/submitting-art/specs/. I want an attractive two sided post card that includes my logo (see attachment). The design would have to have room for the website address, phone number, two location addresses and give them information about a civil action pending against them (You are being sued in X county (case# xxyx). We can help.). I don't really like the visuals of the attached postcard, so please use as a general guide for what I am trying to do. Ultimately, I want an ad that gets people to call me so I can help them.

I also want it to be compatible with the website (LoanHarbor.Legal).

Target Market(s)

Potential bankruptcy clients.

Industry/Entity Type

Legal

Colors

Designer to choose colors to be used in the design.

Requirements
Must have
• Phone number, addresses, website, and place for text regarding pending legal action against the receiver. Should say something to the effect: You have a pending legal action in (county name) County (court name [superior, magistrate, ect.]). Let us help you deal with it responsibly.
• Please note the design specifications at this link:

```html
<!DOCTYPE html>
<html lang="en">
<head>
<meta charset="utf-8">
<title>LoanHarbor Law Group – Bankruptcy Mailer Postcard</title>
<link href="https://fonts.googleapis.com/css2?family=Roboto:wght@400;500;700;900&family=Roboto+Condensed:wght@400;700&display=swap" rel="stylesheet">
<style>
  :root{
    --green:#7cbf6a;
    --green-dark:#4f9a45;
    --green-pale:#d7ecd0;
    --charcoal:#3b3d3f;
    --ink:#2f3133;
    --grey:#7a7d80;
    --paper:#ffffff;
    --stage:#eef0f1;
  }
  *{box-sizing:border-box;margin:0;padding:0}
  html,body{width:1200px;height:900px;overflow:hidden;background:var(--stage)}
  body{font-family:"Roboto",Arial,sans-serif;color:var(--ink);position:relative}
  .card{position:absolute;top:249px;width:570px;height:402px;background:var(--paper);overflow:hidden;box-shadow:0 6px 18px rgba(0,0,0,.15)}
  .card--front{left:20px}
  .card--back{left:610px}
  address{font-style:normal}

  /* shared */
  .brand{position:absolute;display:flex;align-items:center;gap:7px}
  .brand__dot{border-radius:50%;background:var(--green);flex:none}
  .brand__name{font-weight:700;color:var(--green-dark);white-space:nowrap}
  .band{position:absolute;left:0;bottom:0;width:100%}

  /* front */
  .front .brand{top:20px;right:24px}
  .front .brand__dot{width:26px;height:26px}
  .front .brand__name{font-size:17px}
  .hero-photo{position:absolute;left:28px;top:40px;width:205px;height:262px}
  .headline{position:absolute;right:24px;top:82px;text-align:right;font-family:"Roboto Condensed",Arial,sans-serif;line-height:1}
  .headline__main{font-size:44px;font-weight:700;color:var(--ink)}
  .headline__sub{font-size:26px;color:var(--ink);margin-top:4px}
  .headline__sub em{font-style:normal;color:var(--green)}
  .headline__cta{font-size:23px;font-weight:700;color:var(--ink);margin-top:4px;letter-spacing:.3px}
  .offers{position:absolute;top:200px;left:258px;display:flex;gap:12px}
  .offer{width:112px;height:56px;border-radius:6px;background:var(--green);color:#fff;font-family:"Roboto Condensed",Arial,sans-serif;font-weight:700;font-size:17px;line-height:1.05;display:flex;align-items:center;justify-content:center;text-align:center}
  .front-contact{position:absolute;left:362px;top:266px;font-size:7px;line-height:1.45;color:var(--grey)}
  .front-band-text{position:absolute;left:20px;bottom:16px;color:#fff;font-size:12px;line-height:1.45}

  /* back */
  .back-photo{position:absolute;left:0;top:0;width:245px;height:122px}
  .back .brand{top:30px;left:262px}
  .back .brand__dot{width:14px;height:14px}
  .back .brand__name{font-size:10px}
  .return-address{position:absolute;left:420px;top:28px;width:66px;font-size:5.5px;line-height:1.4;color:var(--grey)}
  .stamp{position:absolute;right:22px;top:18px;width:56px;height:62px;border:1.5px solid #9a9da0}
  .address-lines{position:absolute;left:362px;top:132px;width:180px}
  .address-lines span{display:block;height:1px;background:#b9bcbf;margin-bottom:15px}
  .offer-title{position:absolute;left:20px;top:128px;width:300px;font-family:"Roboto Condensed",Arial,sans-serif;font-size:17px;font-weight:700;line-height:1.15;color:var(--green-dark)}
  .offer-copy{position:absolute;left:20px;top:172px;width:290px;font-size:6.5px;line-height:1.45;color:var(--ink)}
  .lawsuit-notice{position:absolute;left:20px;top:200px;width:290px;font-size:7px;line-height:1.4;font-weight:700;color:var(--green-dark)}
  .perks{position:absolute;top:226px;list-style:none;font-size:6.8px;line-height:1.6;color:var(--ink)}
  .perks li::before{content:"";display:inline-block;width:4px;height:4px;background:var(--green-dark);margin-right:4px;vertical-align:middle}
  .perks--left{left:22px}
  .perks--right{left:178px}
  .fine-print{position:absolute;left:22px;top:278px;width:290px;font-size:4.6px;line-height:1.45;color:var(--grey)}
  .call{position:absolute;left:22px;bottom:10px;color:#fff}
  .call__label{font-size:8px}
  .call__phone{display:flex;align-items:center;gap:5px;font-family:"Roboto Condensed",Arial,sans-serif;font-size:23px;font-weight:700;line-height:1.05}
  .call__web{font-size:7.5px;margin-top:2px}
</style>
</head>
<body>

<section class="card card--front front" aria-label="Postcard front">
  <svg class="hero-photo" viewBox="0 0 205 262">
    <defs>
      <linearGradient id="skyFill" x1="0" y1="0" x2="0" y2="1">
        <stop offset="0" stop-color="#e9eef2"/>
        <stop offset=".6" stop-color="#b7c0c8"/>
        <stop offset="1" stop-color="#5c6166"/>
      </linearGradient>
    </defs>
    <path d="M102 6 C140 20 175 24 199 20 C200 120 185 205 102 256 C20 205 5 120 6 20 C30 24 64 20 102 6 Z" fill="var(--green)"/>
    <path role="img" aria-label="Photo of a businessman stretching his arms wide in front of a bright city skyline" d="M102 16 C136 28 166 32 189 29 C189 122 175 198 102 244 C30 198 16 122 16 29 C38 32 68 28 102 16 Z" fill="url(#skyFill)"/>
  </svg>

  <div class="brand"><span class="brand__dot"></span><span class="brand__name">LoanHarbor Law Group</span></div>

  <div class="headline">
    <div class="headline__main">Working Hard?</div>
    <div class="headline__sub">Still Having <em>Money Troubles?</em></div>
    <div class="headline__cta">BANKRUPTCY CAN HELP</div>
  </div>

  <div class="offers">
    <div class="offer">NO CASH<br>UPFRONT</div>
    <div class="offer">OPTIONS<br>FOR FILING</div>
  </div>

  <address class="front-contact">
    Harlow &amp; Associates<br>
    410 Maple Street, Kansas City, MO 64111<br>
    913-555-0187<br>
    www.LoanHarbor.Legal
  </address>

  <svg class="band" viewBox="0 0 570 120" height="120" aria-hidden="true">
    <path d="M0 40 C150 88 330 62 570 6 L570 120 L0 120 Z" fill="var(--green)"/>
    <path d="M0 52 C160 98 340 74 570 20 L570 120 L0 120 Z" fill="var(--charcoal)"/>
  </svg>
  <p class="front-band-text">Don't let them foreclose, repo or garnish your wages!<br>Call Now for a Free Consultation</p>
</section>

<section class="card card--back back" aria-label="Postcard back">
  <svg class="back-photo" viewBox="0 0 245 122" role="img" aria-label="Photo of a mortgage loan modification form on a desk">
    <defs>
      <linearGradient id="deskFill" x1="0" y1="0" x2="1" y2="1">
        <stop offset="0" stop-color="#f4f4f2"/>
        <stop offset="1" stop-color="#b9bbb8"/>
      </linearGradient>
    </defs>
    <rect width="245" height="122" fill="url(#deskFill)"/>
  </svg>

  <svg class="band" viewBox="0 0 570 402" height="402" style="top:0" aria-hidden="true">
    <path d="M0 108 C120 98 230 92 300 96 C330 190 330 260 310 330 L0 330 Z" fill="var(--green-pale)"/>
    <path d="M0 104 C120 92 230 86 300 92 L300 104 C230 98 120 104 0 118 Z" fill="var(--green)"/>
    <path d="M0 318 C200 308 400 272 570 240 L570 402 L0 402 Z" fill="var(--green)"/>
    <path d="M0 330 C200 320 400 286 570 254 L570 402 L0 402 Z" fill="var(--charcoal)"/>
  </svg>

  <div class="brand"><span class="brand__dot"></span><span class="brand__name">LoanHarbor Law Group</span></div>
  <address class="return-address">
    Harlow &amp; Associates<br>410 Maple Street<br>Kansas City, MO 64111
  </address>
  <div class="stamp" aria-label="Postage area"></div>
  <div class="address-lines" aria-label="Recipient address"><span></span><span></span><span></span><span></span></div>

  <h2 class="offer-title">If You Qualify, You Can File<br>Bankruptcy For $0 Upfront!</h2>
  <p class="offer-copy">If you're deep in debt and facing trouble managing your mortgage and other bills, most law firms will recommend that you file for bankruptcy. We're different: we help you file with no money down so you can start fresh.</p>
  <p class="lawsuit-notice">You have a pending legal action in ____________ County (____________ Court, Case # ________). Let us help you deal with it responsibly.</p>

  <ul class="perks perks--left">
    <li>Affordable Re-Payment Plans</li>
    <li>No Money Down Options</li>
    <li>Evening &amp; Weekend Hours</li>
    <li>No Need To Miss Work!</li>
  </ul>
  <ul class="perks perks--right">
    <li>Child Friendly Office</li>
    <li>Bankruptcy Expertise</li>
    <li>It's All We Do!</li>
  </ul>

  <p class="fine-print">The choice of a lawyer is an important decision and should not be based solely upon advertisements. We are a debt relief agency helping people file for relief under the Bankruptcy Code.</p>

  <div class="call">
    <div class="call__label">Call Today</div>
    <div class="call__phone">
      <svg width="16" height="16" viewBox="0 0 24 24" aria-hidden="true"><path fill="#fff" d="M6.6 10.8a15.1 15.1 0 0 0 6.6 6.6l2.2-2.2c.3-.3.7-.4 1-.2 1.1.4 2.3.6 3.6.6.6 0 1 .4 1 1V20c0 .6-.4 1-1 1C10.6 21 3 13.4 3 4c0-.6.4-1 1-1h3.5c.6 0 1 .4 1 1 0 1.3.2 2.5.6 3.6.1.3 0 .7-.2 1z"/></svg>
      913-555-0187
    </div>
    <div class="call__web">www.LoanHarbor.Legal</div>
  </div>
</section>

</body>
</html>
```